Redesign the Eshop of a gift shop

We want to redesign the front page, the category page and the product page of our Eshop that sells gifts.
I am thinking not to reveal the url of the eshop as i don't want you to get influenced. Lets call the Eshop "PresentNest.com"
I will list the brands that we resell so you understand what we are selling,
Morvato-https://www.morvato-example.com/
Zandorpel-https://zandorpel-example.com/
Vamtol - https://vamtol-example.com/
Quiet Orchard - https://www.quietorchard-example.com/
Ranger's Workbench - https://rangersworkbench-example.com/
Plumeline press - https://plumelinepress-example.com/
Tarpawn - https://tarpawnofficial-example.com/
We also sell toys for adults like backgamon, chess, playing cards, board games.
The problem is that many eshops sell these and thats why i would like the design to have a different approach, more fresh, not seen before.
I am also thinking of something playfull, happy, but warm at the same time.
Please note that our logo is black & white but feel free to play with any color/s you like in your website design. We might eventually even adjust the logo colors, or you can provide a pallete that suites a black and white logo
Let me know if you have any questions!
Updates
A couple of designers kindly asked to extend so they can submit.
Target Market(s)
Age: 20-50, Gender: Also men but mostly women, Income: Moderate to high, Interests and Lifestyle: Customers who value sentimentality, personal connection, and thoughtful gestures, Relationship Status: Those in relationships or with larger families
Number of Pages Required
3 page
Look and feel
Each slider illustrates characteristics of the customer's brand and the style your logo design should communicate.

```html
<!DOCTYPE html>
<html lang="en">
<head>
<meta charset="utf-8">
<title>PresentNest – Home</title>
<link href="https://fonts.googleapis.com/css2?family=Nunito:wght@400;600;700;800&family=Kaushan+Script&family=Special+Elite&display=swap" rel="stylesheet">
<style>
:root{
  --coral:#f36c6c;
  --coral-dark:#e55656;
  --ink:#1d1d1d;
  --muted:#8a8a8a;
  --line:#ececec;
  --soft:#f4f4f4;
  --white:#ffffff;
  --black:#0d0d0d;
  --star:#f2a93b;
}
*{box-sizing:border-box;margin:0;padding:0}
html,body{width:1200px;height:3704px;overflow:hidden}
body{font-family:"Nunito",sans-serif;color:var(--ink);background:var(--white);position:relative}
a{color:inherit;text-decoration:none}
.btn{display:inline-block;background:var(--coral);color:var(--white);font-size:10px;font-weight:800;letter-spacing:1px;text-transform:uppercase;padding:12px 26px}
.label{font-family:"Special Elite",monospace;text-transform:uppercase;letter-spacing:2px}

/* header */
.site-header{position:absolute;top:0;left:0;width:1200px;height:80px;display:flex;align-items:center;padding:0 100px;justify-content:space-between;background:var(--white);z-index:2}
.brand{font-family:"Kaushan Script",cursive;font-size:32px;color:var(--coral)}
.main-nav{display:flex;gap:30px;font-size:14px;font-weight:600}
.main-nav a.active{color:var(--coral)}
.header-icons{display:flex;gap:16px}
.header-icons svg{width:16px;height:16px;stroke:var(--ink);fill:none;stroke-width:2}

/* hero */
.hero{position:absolute;top:80px;left:0;width:1200px;height:568px;background:linear-gradient(100deg,#c9c4c2 0%,#e6e1de 45%,#d8cfcb 70%,#b9aeaa 100%)}
.hero-photo{position:absolute;right:150px;top:0;width:520px;height:568px;background:radial-gradient(ellipse at 55% 40%,#d0353f 0%,#b52a34 22%,rgba(222,214,210,.0) 48%)}
.hero-copy{position:absolute;left:100px;top:150px;color:var(--white)}
.hero-copy .label{font-size:18px}
.hero-copy h1{font-size:60px;font-weight:700;margin:10px 0 14px;letter-spacing:-.5px}
.hero-copy p{font-size:14px;width:340px;line-height:1.5}
.hero-copy .btn{margin-top:30px}

/* promos */
.promos{position:absolute;top:728px;left:100px;width:1000px;display:flex;gap:28px}
.promo{flex:1;height:304px;background:var(--soft);position:relative;padding:54px 34px}
.promo-copy{position:relative;z-index:1;width:250px}
.promo .label{font-size:13px}
.promo h3{color:var(--coral);font-size:20px;font-weight:800;margin:14px 0 8px;white-space:nowrap}
.promo p{font-size:12px;color:var(--muted);width:210px;line-height:1.45}
.promo .btn{margin-top:28px}
.promo-art{position:absolute;right:18px;top:28px;width:170px;height:250px;border-radius:6px}
.art-xmas{background:linear-gradient(160deg,#3f8a3b,#c7302f 70%,#f2f2f2)}
.art-bday{background:linear-gradient(160deg,#f5c542,#e24b5c 55%,#4aa4d8)}

/* section heading */
.section-title{position:absolute;left:0;width:1200px;text-align:center;font-size:38px;font-weight:800}

/* product cards */
.product-grid{position:absolute;top:1232px;left:100px;width:1000px;display:grid;grid-template-columns:repeat(4,1fr);gap:36px 18px}
.product-card{height:340px;border:1px solid var(--line);position:relative;padding:28px 20px 0;text-align:left}
.product-card .thumb{width:170px;height:180px;margin:0 auto;border-radius:4px;background:radial-gradient(circle at 50% 55%,#d49a5f 0%,#b7773f 45%,#f4ede6 72%)}
.card-icons{position:absolute;right:12px;top:14px;display:flex;flex-direction:column;gap:6px}
.card-icons svg{width:14px;height:14px;stroke:#b5b5b5;fill:none;stroke-width:1.8}
.product-card h4{font-size:17px;font-weight:700;margin:22px 0 6px;text-align:center}
.price{text-align:center;font-size:15px}
.price s{color:var(--muted);font-size:12px;margin-right:8px}
.price strong{color:var(--coral);font-weight:700}
.stars{text-align:center;color:var(--star);font-size:13px;letter-spacing:2px;margin-top:6px}

.view-all{position:absolute;top:2008px;left:0;width:1200px;text-align:center}

/* banner */
.gift-banner{position:absolute;top:2112px;left:0;width:1200px;height:328px;background:var(--coral)}
.gift-banner .copy{position:absolute;left:214px;top:70px;color:var(--white);z-index:1}
.gift-banner .label{font-size:15px}
.gift-banner h2{font-size:37px;font-weight:800;line-height:1.2;margin:14px 0 26px;width:460px}
.gift-banner .btn{background:transparent;border:1px solid var(--white);padding:10px 24px}
.banner-art{position:absolute;right:190px;top:-20px;width:300px;height:330px;background:radial-gradient(ellipse at 50% 60%,#d9232e 0%,#c41d2a 40%,rgba(243,108,108,0) 70%)}

/* popular carousel */
.carousel{position:absolute;top:2620px;left:100px;width:1000px;height:340px}
.carousel-track{position:absolute;left:60px;width:880px;display:flex;gap:24px}
.carousel .product-card{flex:0 0 277px}
.carousel .product-card .thumb{background:radial-gradient(circle at 50% 60%,#2a2622 0%,#7e6a52 40%,#f3efe9 72%)}
.carousel-arrow{position:absolute;top:140px;width:34px;height:34px;border-radius:50%;background:#ffe5e5;display:flex;align-items:center;justify-content:center}
.carousel-arrow svg{width:14px;height:14px;stroke:var(--coral);fill:none;stroke-width:2.5}
.arrow-prev{left:0}.arrow-next{right:0}

/* newsletter & footer */
.site-footer{position:absolute;top:3160px;left:0;width:1200px;height:544px;background:var(--black);color:var(--white)}
.newsletter{position:absolute;top:3040px;left:168px;width:864px;height:264px;background:var(--coral);text-align:center;color:var(--white);padding-top:56px;z-index:1}
.newsletter .label{font-size:14px}
.newsletter h2{font-size:26px;font-weight:800;line-height:1.25;margin:14px auto 22px;width:360px}
.signup{display:flex;justify-content:center}
.signup span{width:300px;height:42px;background:var(--white);color:#aaa;font-size:11px;text-align:left;padding:14px 16px}
.signup .btn{height:42px;border:2px solid var(--white);padding:13px 26px}
.footer-cols{position:absolute;top:192px;left:100px;width:1000px;display:flex}
.footer-about{width:340px}
.footer-about .brand{color:var(--white);font-size:40px}
.footer-about p{font-size:12px;line-height:1.55;color:#cfcfcf;width:220px;margin-top:16px}
.footer-col{width:200px}
.footer-col.contact{width:260px}
.footer-col h5{font-size:17px;font-weight:700;margin-bottom:26px}
.footer-col li{list-style:none;font-size:12px;color:#cfcfcf;margin-bottom:10px}
.contact li{display:flex;align-items:center;gap:10px;white-space:nowrap;font-size:11.5px}
.contact i{flex:0 0 22px;width:22px;height:22px;border-radius:50%;border:1px solid #777;display:flex;align-items:center;justify-content:center}
.contact svg{width:10px;height:10px;stroke:var(--white);fill:none;stroke-width:2}
.footer-bottom{position:absolute;left:100px;top:472px;width:1000px;border-top:1px solid #333;padding-top:22px;display:flex;justify-content:space-between;font-size:12px;color:#cfcfcf}
</style>
</head>
<body>

<header class="site-header">
  <a class="brand" href="#">PresentNest</a>
  <nav class="main-nav">
    <a class="active" href="#">Home</a><a href="#">Categories</a><a href="#">Shop</a><a href="#">About Us</a><a href="#">Contact</a>
  </nav>
  <div class="header-icons">
    <svg viewBox="0 0 24 24"><circle cx="11" cy="11" r="7"/><path d="M16 16l5 5"/></svg>
    <svg viewBox="0 0 24 24"><circle cx="12" cy="8" r="4"/><path d="M4 21c1-5 15-5 16 0"/></svg>
    <svg viewBox="0 0 24 24"><path d="M12 20S3 14 3 8a4.5 4.5 0 0 1 9-1 4.5 4.5 0 0 1 9 1c0 6-9 12-9 12z"/></svg>
    <svg viewBox="0 0 24 24"><path d="M3 4h3l2 12h11l2-8H7"/><circle cx="9" cy="20" r="1.4"/><circle cx="18" cy="20" r="1.4"/></svg>
  </div>
</header>

<section class="hero">
  <div class="hero-photo" role="img" aria-label="Hands in a knit sweater holding a gift wrapped in red with a ribbon bow"></div>
  <div class="hero-copy">
    <div class="label">Christmas Special</div>
    <h1>New Collections</h1>
    <p>Thoughtful gifts picked with care for family, friends and every festive moment this season.</p>
    <a class="btn" href="#">Shop Now</a>
  </div>
</section>

<section class="promos">
  <article class="promo">
    <div class="promo-copy">
      <div class="label">Christmas Special</div>
      <h3>Latest Gift Collections</h3>
      <p>Cosy holiday finds chosen to warm up every home.</p>
      <a class="btn" href="#">Shop Now</a>
    </div>
    <div class="promo-art art-xmas" role="img" aria-label="Festive Christmas tree with gifts illustration"></div>
  </article>
  <article class="promo">
    <div class="promo-copy">
      <div class="label">Birthday Special</div>
      <h3>Latest Gift Collections</h3>
      <p>Bright party gifts to make every birthday shine.</p>
      <a class="btn" href="#">Shop Now</a>
    </div>
    <div class="promo-art art-bday" role="img" aria-label="Colourful balloons and wrapped birthday presents"></div>
  </article>
</section>

<h2 class="section-title" style="top:1128px">Latest Products</h2>

<section class="product-grid">
  <article class="product-card"><div class="card-icons"><svg viewBox="0 0 24 24"><path d="M12 20S3 14 3 8a4.5 4.5 0 0 1 9-1 4.5 4.5 0 0 1 9 1c0 6-9 12-9 12z"/></svg><svg viewBox="0 0 24 24"><path d="M2 12s4-7 10-7 10 7 10 7-4 7-10 7S2 12 2 12z"/><circle cx="12" cy="12" r="3"/></svg></div><div class="thumb" role="img" aria-label="Cardboard box filled with baby toys"></div><h4>Baby Toy Bundle</h4><div class="price"><s>$98.00</s><strong>$49.99</strong></div><div class="stars">★★★★★</div></article>
  <article class="product-card"><div class="card-icons"><svg viewBox="0 0 24 24"><path d="M12 20S3 14 3 8a4.5 4.5 0 0 1 9-1 4.5 4.5 0 0 1 9 1c0 6-9 12-9 12z"/></svg><svg viewBox="0 0 24 24"><path d="M2 12s4-7 10-7 10 7 10 7-4 7-10 7S2 12 2 12z"/><circle cx="12" cy="12" r="3"/></svg></div><div class="thumb" role="img" aria-label="Cardboard box filled with baby toys"></div><h4>Baby Toy Bundle</h4><div class="price"><s>$98.00</s><strong>$49.99</strong></div><div class="stars">★★★★★</div></article>
  <article class="product-card"><div class="card-icons"><svg viewBox="0 0 24 24"><path d="M12 20S3 14 3 8a4.5 4.5 0 0 1 9-1 4.5 4.5 0 0 1 9 1c0 6-9 12-9 12z"/></svg><svg viewBox="0 0 24 24"><path d="M2 12s4-7 10-7 10 7 10 7-4 7-10 7S2 12 2 12z"/><circle cx="12" cy="12" r="3"/></svg></div><div class="thumb" role="img" aria-label="Cardboard box filled with baby toys"></div><h4>Baby Toy Bundle</h4><div class="price"><s>$98.00</s><strong>$49.99</strong></div><div class="stars">★★★★★</div></article>
  <article class="product-card"><div class="card-icons"><svg viewBox="0 0 24 24"><path d="M12 20S3 14 3 8a4.5 4.5 0 0 1 9-1 4.5 4.5 0 0 1 9 1c0 6-9 12-9 12z"/></svg><svg viewBox="0 0 24 24"><path d="M2 12s4-7 10-7 10 7 10 7-4 7-10 7S2 12 2 12z"/><circle cx="12" cy="12" r="3"/></svg></div><div class="thumb" role="img" aria-label="Cardboard box filled with baby toys"></div><h4>Baby Toy Bundle</h4><div class="price"><s>$98.00</s><strong>$49.99</strong></div><div class="stars">★★★★★</div></article>
  <article class="product-card"><div class="card-icons"><svg viewBox="0 0 24 24"><path d="M12 20S3 14 3 8a4.5 4.5 0 0 1 9-1 4.5 4.5 0 0 1 9 1c0 6-9 12-9 12z"/></svg><svg viewBox="0 0 24 24"><path d="M2 12s4-7 10-7 10 7 10 7-4 7-10 7S2 12 2 12z"/><circle cx="12" cy="12" r="3"/></svg></div><div class="thumb" role="img" aria-label="Cardboard box filled with baby toys"></div><h4>Baby Toy Bundle</h4><div class="price"><s>$98.00</s><strong>$49.99</strong></div><div class="stars">★★★★★</div></article>
  <article class="product-card"><div class="card-icons"><svg viewBox="0 0 24 24"><path d="M12 20S3 14 3 8a4.5 4.5 0 0 1 9-1 4.5 4.5 0 0 1 9 1c0 6-9 12-9 12z"/></svg><svg viewBox="0 0 24 24"><path d="M2 12s4-7 10-7 10 7 10 7-4 7-10 7S2 12 2 12z"/><circle cx="12" cy="12" r="3"/></svg></div><div class="thumb" role="img" aria-label="Cardboard box filled with baby toys"></div><h4>Baby Toy Bundle</h4><div class="price"><s>$98.00</s><strong>$49.99</strong></div><div class="stars">★★★★★</div></article>
  <article class="product-card"><div class="card-icons"><svg viewBox="0 0 24 24"><path d="M12 20S3 14 3 8a4.5 4.5 0 0 1 9-1 4.5 4.5 0 0 1 9 1c0 6-9 12-9 12z"/></svg><svg viewBox="0 0 24 24"><path d="M2 12s4-7 10-7 10 7 10 7-4 7-10 7S2 12 2 12z"/><circle cx="12" cy="12" r="3"/></svg></div><div class="thumb" role="img" aria-label="Cardboard box filled with baby toys"></div><h4>Baby Toy Bundle</h4><div class="price"><s>$98.00</s><strong>$49.99</strong></div><div class="stars">★★★★★</div></article>
  <article class="product-card"><div class="card-icons"><svg viewBox="0 0 24 24"><path d="M12 20S3 14 3 8a4.5 4.5 0 0 1 9-1 4.5 4.5 0 0 1 9 1c0 6-9 12-9 12z"/></svg><svg viewBox="0 0 24 24"><path d="M2 12s4-7 10-7 10 7 10 7-4 7-10 7S2 12 2 12z"/><circle cx="12" cy="12" r="3"/></svg></div><div class="thumb" role="img" aria-label="Cardboard box filled with baby toys"></div><h4>Baby Toy Bundle</h4><div class="price"><s>$98.00</s><strong>$49.99</strong></div><div class="stars">★★★★★</div></article>
</section>

<div class="view-all"><a class="btn" href="#">View All Products</a></div>

<section class="gift-banner">
  <div class="copy">
    <div class="label">Surprise Your Friends and Family</div>
    <h2>Check Out Our Hot Gift Collections</h2>
    <a class="btn" href="#">Shop Now</a>
  </div>
  <div class="banner-art" role="img" aria-label="Stack of red gift boxes tied with gold ribbons"></div>
</section>

<h2 class="section-title" style="top:2520px">Popular Products</h2>

<section class="carousel">
  <a class="carousel-arrow arrow-prev" href="#"><svg viewBox="0 0 24 24"><path d="M15 5l-7 7 7 7"/></svg></a>
  <div class="carousel-track">
    <article class="product-card"><div class="card-icons"><svg viewBox="0 0 24 24"><path d="M12 20S3 14 3 8a4.5 4.5 0 0 1 9-1 4.5 4.5 0 0 1 9 1c0 6-9 12-9 12z"/></svg><svg viewBox="0 0 24 24"><path d="M2 12s4-7 10-7 10 7 10 7-4 7-10 7S2 12 2 12z"/><circle cx="12" cy="12" r="3"/></svg></div><div class="thumb" role="img" aria-label="Set of wooden chess pieces"></div><h4>Chessboard</h4><div class="price"><s>$98.00</s><strong>$49.99</strong></div><div class="stars">★★★★★</div></article>
    <article class="product-card"><div class="card-icons"><svg viewBox="0 0 24 24"><path d="M12 20S3 14 3 8a4.5 4.5 0 0 1 9-1 4.5 4.5 0 0 1 9 1c0 6-9 12-9 12z"/></svg><svg viewBox="0 0 24 24"><path d="M2 12s4-7 10-7 10 7 10 7-4 7-10 7S2 12 2 12z"/><circle cx="12" cy="12" r="3"/></svg></div><div class="thumb" role="img" aria-label="Set of wooden chess pieces"></div><h4>Chessboard</h4><div class="price"><s>$98.00</s><strong>$49.99</strong></div><div class="stars">★★★★★</div></article>
    <article class="product-card"><div class="card-icons"><svg viewBox="0 0 24 24"><path d="M12 20S3 14 3 8a4.5 4.5 0 0 1 9-1 4.5 4.5 0 0 1 9 1c0 6-9 12-9 12z"/></svg><svg viewBox="0 0 24 24"><path d="M2 12s4-7 10-7 10 7 10 7-4 7-10 7S2 12 2 12z"/><circle cx="12" cy="12" r="3"/></svg></div><div class="thumb" role="img" aria-label="Set of wooden chess pieces"></div><h4>Chessboard</h4><div class="price"><s>$98.00</s><strong>$49.99</strong></div><div class="stars">★★★★★</div></article>
  </div>
  <a class="carousel-arrow arrow-next" href="#"><svg viewBox="0 0 24 24"><path d="M9 5l7 7-7 7"/></svg></a>
</section>

<section class="newsletter">
  <div class="label">Newsletter</div>
  <h2>Subscribe To Our To Get Latest News And Offers!</h2>
  <div class="signup"><span>Enter your email address</span><a class="btn" href="#">Subscribe</a></div>
</section>

<footer class="site-footer">
  <div class="footer-cols">
    <div class="footer-about">
      <div class="brand">PresentNest</div>
      <p>Gifts chosen with heart for the people you love. Warm finds, playful games and small surprises for every special day of the year.</p>
    </div>
    <div class="footer-col"><h5>Quick Links</h5><ul><li>Home</li><li>About</li><li>Categories</li><li>Shop</li><li>Contact</li></ul></div>
    <div class="footer-col"><h5>Categories</h5><ul><li>Categorie 01</li><li>Categorie 02</li><li>Categorie 03</li><li>Categorie 04</li></ul></div>
    <div class="footer-col contact"><h5>Get In Touch</h5><ul>
      <li><i><svg viewBox="0 0 24 24"><path d="M5 3h4l2 5-3 2a11 11 0 0 0 6 6l2-3 5 2v4a2 2 0 0 1-2 2A18 18 0 0 1 3 5a2 2 0 0 1 2-2z"/></svg></i>Call: +1 555-014-2290</li>
      <li><i><svg viewBox="0 0 24 24"><rect x="4" y="8" width="16" height="11"/><path d="M7 8V3h10v5"/></svg></i>Fax: +1 555-014-7731</li>
      <li><i><svg viewBox="0 0 24 24"><rect x="3" y="5" width="18" height="14"/><path d="M3 6l9 7 9-7"/></svg></i>Email: hello@presentnest-example.com</li>
    </ul></div>
  </div>
  <div class="footer-bottom">
    <span>© 2022-2025. PresentNest All rights reserved</span>
    <span>Site map | Terms and conditions | Privacy Policy</span>
  </div>
</footer>

</body>
</html>
```